Website Design for a High School

School Name: Bayt Nakhla Private Schools
sub-schools:
1-Bayt Nakhla Primary School
2-Bayt Nakhla High School for Girls
3-Bayt Nakhla High School for Boys
The design should be professional and serious and below is the details of the website.
Pages: (Home, About Us, Schools, Events, Students, Gallery, Lectures, Contact Us).
A-) Home Page:
1-Animated photos banner as main
2-Marquee for the last news.
3-Welcoming block of text
4-latest news at the body of the page.
5-Calender "on the side"
6-Number of visitors "on the side"
7-Search bar
8-options to choose a school
B-) School Page:
three schools listed as drop down menu when highlighted over the Schools button in the menu
*Each school page should contain:
1-Student login area
2-Animation photos header
3-Specific news and projects
C-) Student Login page:
have a Report Card
D-) Gallery Page
have a collection of photos.
E-)Contact Page
phone numbers
emails
feedback form
F-)Other mentioned pages
with normal text and photos page look as similar to the Home page.
Required color: Purple as main and include the logo colors
Logo: is attached.
Button link to change language to Arabic.
School
5+ page

```html
<!DOCTYPE html>
<html lang="en">
<head>
<meta charset="utf-8">
<title>Bayt Nakhla High School</title>
<link href="https://fonts.googleapis.com/css2?family=Open+Sans:wght@400;600;700&family=Roboto:wght@300;400&display=swap" rel="stylesheet">
<style>
:root{
  --purple:#6a3f9e;
  --purple-text:#6b3fa0;
  --gold:#f6a800;
  --body:#666;
  --line:#d9d9d9;
  --soft:#f7f7f7;
  --white:#fff;
}
*{box-sizing:border-box;margin:0;padding:0}
html,body{width:901px;height:1200px;overflow:hidden;background:var(--white)}
body{position:relative;font-family:"Open Sans",sans-serif;color:var(--body)}
.abs{position:absolute}

.topbar{left:0;top:0;width:901px;height:31px;background:var(--purple)}
.topbar .blank{left:0;top:0;width:160px;height:31px;background:var(--white)}
.marquee{left:177px;top:8px;font-size:9.5px;color:var(--white);white-space:nowrap}
.select{border:1px solid #ccc;background:var(--white);font-size:9.5px;color:#888;padding:0 8px;display:flex;align-items:center;justify-content:space-between;border-radius:2px}
.select::after{content:"▾";font-size:8px;color:#333}
.lang{left:787px;top:5px;width:78px;height:20px}
.school-pick{left:696px;top:41px;width:169px;height:19px}
.search{left:666px;top:44px}

.logo{left:43px;top:3px;width:102px;height:102px;border-radius:50%;background:var(--white);border:3px solid #3a2a6e;display:flex;align-items:center;justify-content:center;text-align:center;font-family:"Open Sans",sans-serif;font-weight:700;font-size:11px;line-height:14px;color:var(--purple)}

.header-line{left:0;top:104px;width:901px;height:1px;background:#e5e5e5}
.nav{top:78px;left:292px;display:flex;font-size:11px;color:#555}
.nav span{padding:0 14px;border-left:1px solid #ccc;line-height:12px}
.nav span:first-child{border-left:0;color:var(--purple-text);padding-left:0}
.nav span:last-child{padding-right:0}

.hero{left:0;top:105px;width:901px;height:403px;background:linear-gradient(100deg,#c9b9a6 0%,#6b7690 25%,#b9b2a7 45%,#e14b4b 65%,#d9a184 80%,#c5c0bb 100%)}

.welcome-title{left:42px;top:540px;font-family:"Roboto",sans-serif;font-weight:300;font-size:23px;color:var(--purple-text)}
.welcome p{font-size:10.5px;line-height:18px;width:570px}
.welcome{left:42px;top:578px}
.welcome p+p{margin-top:16px}
.read-more{left:42px;top:730px;font-size:10.5px;color:var(--purple-text)}
.welcome-photo{left:625px;top:544px;width:240px;height:177px;border-radius:3px;background:linear-gradient(110deg,#8a7f7a 0%,#c2463d 40%,#d9b08f 65%,#4f9a3c 100%);box-shadow:0 1px 3px rgba(0,0,0,.25)}

.band{left:0;top:767px;width:901px;height:339px;background:var(--soft);border-top:1px solid #eee}
.card{top:794px;height:280px;background:var(--white);border:1px solid #eee;border-radius:4px;box-shadow:0 1px 3px rgba(0,0,0,.08);padding:0 15px}
.card-news-letter{left:51px;width:250px}
.card-news{left:326px;width:250px}
.card-social{left:597px;width:260px}
.card h2{position:absolute;left:62px;top:16px;font-family:"Roboto",sans-serif;font-weight:300;font-size:17.5px;color:var(--purple-text);white-space:nowrap}
.card .icon{position:absolute;left:12px;top:15px;width:34px;height:34px;border-radius:4px;background:linear-gradient(135deg,#cfe3f5,#2f6fb5)}
.card p{font-size:9.5px;line-height:15px}
.label{font-size:10.5px;color:var(--purple-text)}
.field{height:22px;border:1px solid var(--line);margin-top:7px}
.btn{display:inline-block;background:var(--gold);color:var(--white);font-size:9.5px;font-weight:600;padding:4px 11px;border-radius:2px}
.news-head{font-size:12px;color:var(--purple-text);margin-bottom:4px}
.news-age{font-size:10.5px;color:var(--gold);margin-top:6px}
.dots{border-bottom:1px dotted #999;margin:9px 0 10px}

.like{display:inline-block;border:1px solid #c8cfe0;background:#eef1f7;font-size:9px;color:#3b5998;padding:2px 5px;border-radius:2px}
.fans{font-size:8.5px;color:#333;border-top:1px solid var(--line);padding-top:5px}
.avatars{display:grid;grid-template-columns:repeat(4,41px);column-gap:15px;row-gap:4px;margin-top:5px}
.avatar div{width:41px;height:41px}
.avatar span{display:block;text-align:center;font-size:7.5px;color:#666;margin-top:3px}
.plugin{font-size:7.5px;color:#555;border-top:1px solid var(--line);padding-top:3px;margin-top:4px;display:flex;align-items:center;gap:4px;width:220px}
.plugin i{display:inline-block;width:10px;height:10px;background:#3b5998}

.footer{left:0;top:1106px;width:901px;height:94px;background:var(--purple);color:var(--white)}
.fnav{left:42px;top:31px;display:flex;font-size:10.5px}
.fnav span{padding:0 20px;border-left:1px solid rgba(255,255,255,.5);line-height:11px}
.fnav span:first-child{border-left:0;padding-left:0}
.copyright{left:42px;top:62px;font-size:8.5px}
.follow{left:730px;top:32px;font-size:10.5px;display:flex;align-items:center;gap:8px}
.follow .dot{width:20px;height:20px;border-radius:50%;background:var(--white)}
.follow span{margin-right:4px}
.visitors{left:725px;top:62px;display:flex;align-items:center;gap:8px;font-weight:700;font-size:12px}
.counter{background:var(--white);color:#111;font-size:16px;letter-spacing:1.5px;padding:0 8px;height:20px;line-height:20px;border-radius:2px}
</style>
</head>
<body>

<div class="abs topbar">
  <div class="abs blank"></div>
  <div class="abs marquee">Lorem ipsum dolor sit amet, consectetur adipiscing elit, sed do eiusmod tempor incididunt ut labore et dolore magna aliqua. Ut enim</div>
  <div class="abs select lang">Language</div>
</div>

<div class="abs logo">Bayt Nakhla<br>Schools</div>

<svg class="abs search" width="14" height="14" viewBox="0 0 14 14" aria-hidden="true"><circle cx="5.5" cy="5.5" r="4" fill="none" stroke="#aaa" stroke-width="1.6"/><line x1="8.5" y1="8.5" x2="12.5" y2="12.5" stroke="#aaa" stroke-width="1.8"/></svg>
<div class="abs select school-pick">Choose School</div>

<nav class="abs nav">
  <span>Home</span><span>About Us</span><span>Schools</span><span>Events</span><span>Students</span><span>Gallery</span><span>Lectures</span><span>Contact Us</span>
</nav>
<div class="abs header-line"></div>

<div class="abs hero" role="img" aria-label="Banner photo of smiling students sitting together outdoors"></div>

<h1 class="abs welcome-title">Welcome to Bayt Nakhla High School</h1>
<div class="abs welcome">
  <p>Lorem ipsum dolor sit amet, consectetur adipiscing elit, sed do eiusmod tempor incididunt ut labore et dolore magna aliqua. Ut enim ad minim veniam, quis nostrud exercitation ullamco laboris nisi ut aliquip ex ea commodo consequat. Duis aute irure dolor in reprehenderit in voluptate velit esse cillum dolore eu fugiat nulla pariatur. Excepteur sint occaecat cupidatat non proident, sunt in culpa qui officia deserunt mollit anim id est laborum.</p>
  <p>Lorem ipsum dolor sit amet, consectetur adipiscing elit, sed do eiusmod tempor incididunt ut labore et dolore magna aliqua. Ut enim ad minim veniam, quis nostrud exercitation ullamco laboris nisi ut aliquip ex ea commodo consequat. Duis aute irure dolor in reprehenderit in voluptate.</p>
</div>
<div class="abs read-more">Read More</div>
<div class="abs welcome-photo" role="img" aria-label="Photo of students writing at desks in a classroom"></div>

<div class="abs band"></div>

<section class="abs card card-news-letter">
  <div class="icon" role="img" aria-label="Newsletter envelope illustration"></div>
  <h2>Signup For Newsletter</h2>
  <p style="margin-top:71px">Lorem ipsum dolor sit amet, consectetur adipiscing elit, sed do eiusmodLorem ipsum dolor sit amet, consectetur adipiscing.</p>
  <div class="label" style="margin-top:14px">Enter Your Name</div>
  <div class="field"></div>
  <div class="label" style="margin-top:15px">Enter Your Email Address</div>
  <div class="field"></div>
  <div class="btn" style="margin-top:16px">Subscribe</div>
</section>

<section class="abs card card-news">
  <div class="icon" role="img" aria-label="News globe illustration"></div>
  <h2 style="top:19px">Get Latest News</h2>
  <div class="news-head" style="margin-top:61px">Heading goes Here</div>
  <p>Lorem ipsum dolor sit amet, consectetur adipiscing elit, sed do eiusmod consectetur.</p>
  <div class="news-age">5 days ago</div>
  <div class="dots"></div>
  <div class="news-head">Heading goes Here</div>
  <p>Lorem ipsum dolor sit amet, consectetur adipiscing elit, sed do eiusmod consectetur.</p>
  <div class="news-age">5 days ago</div>
  <div class="dots"></div>
  <div class="btn" style="padding:4px 15px">See All</div>
</section>

<section class="abs card card-social">
  <div class="icon" style="width:30px;height:30px;border-radius:0;background:#3b5998"></div>
  <h2 style="left:52px">Bayt Nakhla High School</h2>
  <div style="margin-top:54px"><span class="like">Like</span></div>
  <div class="fans" style="margin-top:6px">4,788,995 people like <b>Nakhla Community Hub</b>.</div>
  <div class="avatars">
    <div class="avatar"><div role="img" aria-label="Member photo" style="background:#4a4a4a"></div><span>Rana</span></div>
    <div class="avatar"><div role="img" aria-label="Member photo" style="background:#c9a48f"></div><span>Basma</span></div>
    <div class="avatar"><div role="img" aria-label="Member photo" style="background:linear-gradient(#c4863a,#2e2a2a)"></div><span>Omar</span></div>
    <div class="avatar"><div role="img" aria-label="Member photo" style="background:#9a6a55"></div><span>Kinda</span></div>
    <div class="avatar"><div role="img" aria-label="Member photo" style="background:#d8b070"></div><span>Jana</span></div>
    <div class="avatar"><div role="img" aria-label="Member photo" style="background:#b89a63"></div><span>Nada</span></div>
    <div class="avatar"><div role="img" aria-label="Member photo" style="background:#3a3232"></div><span>Hala</span></div>
    <div class="avatar"><div role="img" aria-label="Member photo" style="background:linear-gradient(#e0a040,#6b3a1c)"></div><span>Karim</span></div>
  </div>
  <div class="plugin"><i></i>Community social plugin</div>
</section>

<footer class="abs footer">
  <div class="abs fnav">
    <span>Home</span><span>About Us</span><span>Schools</span><span>Events</span><span>Students</span><span>Gallery</span><span>Lectures</span><span>Contact Us</span>
  </div>
  <div class="abs copyright">© copyright 2015 by Bayt Nakhla High School. All rights reserved.</div>
  <div class="abs follow"><span>Follow us</span><div class="dot"></div><div class="dot"></div><div class="dot"></div></div>
  <div class="abs visitors">Visitors <span class="counter">0000000</span></div>
</footer>

</body>
</html>
```